Artwork for pharmaceutical cream against eczema

We are a Belgian company launching a steroid-free cream for itchy, red and eczematic skin. It will be a 50 ml tube in a cardboard box. We are looking for a reliable, pharmaceutical, yet no sterile clinical, feel. A product a pharmacist would recommend, but you would not find in a general drug store or perfume shop. The name of the product is "Dremou". Colors to be used are deep blue, orange, black and white. The main color should not be black or white. The prominent use of the capital "S", like in the Quenbor example should be considered. A design with a curved element that goes with the S, like in the Vitamin C example has the preference.

Reason: Hi all, I will extend the deadline with 5 days, because we feel that there is still not a perfect fit. Thanks Gijs

Target Market(s)

Pharmacy. Broad public. Young parents with growing children.

Industry/Entity Type

Pharmacy

Font styles to use
Sans Serif

Requirements
Must have
• Text elements:
• "Dremou® crème"
• "50 g"
• "Bevat 1% hatseflats"
• "Verzorging van jeukende, rode en geïrriteerde huid"
Nice to have
• Side text elements (in plain black):
• "Lot 17XX17"
• "EXP 04/2020"
• Dummy EAN-13 barcode
• "Tirdu bvba - Dremoustraat 15 - 1234 Antwerpen"
• "Bevat Lorem ipsum dolor sit amet, consectetur adipiscing elit, sed do eiusmod tempor incididunt ut labore et dolore magna aliqua"

```html
<!DOCTYPE html>
<html lang="nl">
<head>
<meta charset="utf-8">
<title>Dremou crème – verpakking voorzijde</title>
<link rel="stylesheet" href="https://fonts.googleapis.com/css2?family=Lexend:wght@400;500&display=swap">
<style>
  :root {
    --canvas-bg: #ffffff;
    --pack-grey: #e4e5e9;
    --pack-orange: #c25a0c;
    --pack-white: #ffffff;
    --brand-navy: #1d2857;
    --text-slate: #3a3f5c;
  }
  * { margin: 0; padding: 0; box-sizing: border-box; }
  html, body {
    width: 1200px;
    height: 534px;
    overflow: hidden;
    background: var(--canvas-bg);
    font-family: "Lexend", "Helvetica Neue", Arial, sans-serif;
  }
  .canvas {
    position: relative;
    width: 1200px;
    height: 534px;
  }
  .pack-front {
    position: absolute;
    left: 74px;
    top: 152px;
    width: 1080px;
    height: 254px;
    background: var(--pack-grey);
    overflow: hidden;
  }
  .pack-band {
    position: absolute;
    inset: 0;
    width: 1080px;
    height: 254px;
  }
  .pack-band .band-orange { fill: var(--pack-orange); }

  .claim-badge {
    position: absolute;
    left: 805px;
    top: 25px;
    width: 232px;
    height: 29px;
    border: 1.5px solid var(--pack-white);
    border-radius: 7px;
    color: var(--pack-white);
    font-size: 16px;
    font-weight: 400;
    line-height: 26px;
    text-align: center;
  }

  .product-name {
    position: absolute;
    left: 58px;
    top: 150px;
    color: var(--brand-navy);
    font-size: 46px;
    font-weight: 500;
    line-height: 1;
    white-space: nowrap;
  }

  .product-info {
    position: absolute;
    right: 28px;
    top: 176px;
    display: flex;
    align-items: flex-end;
    color: var(--text-slate);
  }
  .product-claim {
    font-size: 18.5px;
    font-weight: 400;
    line-height: 22px;
    text-align: right;
    padding-right: 8px;
  }
  .product-size {
    border-left: 1.5px solid var(--text-slate);
    padding-left: 7px;
    height: 26px;
    font-size: 20px;
    font-weight: 500;
    line-height: 28px;
    color: var(--brand-navy);
  }
</style>
</head>
<body>
<main class="canvas">
  <section class="pack-front" aria-label="Dremou crème verpakking">
    <svg class="pack-band" viewBox="0 0 1080 254" aria-hidden="true">
      <path class="band-orange" d="M0 0 H1080 V92 Q540 150 0 92 Z"/>
    </svg>

    <div class="claim-badge">Bevat 1% hatseflats</div>

    <h1 class="product-name">Dremou® crème</h1>

    <div class="product-info">
      <p class="product-claim">Verzorging van jeukende, rode en<br>geïrriteerde huid</p>
      <p class="product-size">50 g</p>
    </div>
  </section>
</main>
</body>
</html>
```